꽃차 제조 회사입니다.
경북 영주 소백산 아래에 유기농 농장에서 약재청에 등록이 되어 있는 꽃들로만 꽃차를 만드는 프리미엄 꽃차 입니다.
현재 패키지 중 명절 선물세트 겉 슬리브 디자인을 원합니다.
현재 패키지 디자인은 나와 있으며
이것과 어울리는 명절 (추석 &설) 세트 이미지가 필요합니다.
상자에 끼우는 슬리브 형태의 패키지 입니다.

```html
<!DOCTYPE html>
<html lang="ko">
<head>
<meta charset="utf-8">
<title>위드그린데이 명절 선물세트 슬리브</title>
<link href="https://fonts.googleapis.com/css2?family=Noto+Serif+KR:wght@400;500&family=Cormorant+Garamond:wght@500;600&display=swap" rel="stylesheet">
<style>
  :root {
    --page: #ffffff;
    --ink: #8a6a4c;
    --ink-soft: #a08870;
    --band: #ffffff;
    --lace: #e6e6ea;
    --pink: #f4b6cf;
    --lilac: #c9c2ea;
    --sky: #cfe1f3;
    --butter: #f8edc6;
    --cream: #fbe6cf;
    --rose: #e890b4;
  }
  html, body {
    margin: 0;
    padding: 0;
    width: 1200px;
    height: 1200px;
    overflow: hidden;
    background: var(--page);
  }
  .canvas {
    position: relative;
    width: 1200px;
    height: 1200px;
    background: var(--page);
  }
  .top-lace {
    position: absolute;
    left: 370px;
    top: 0;
    width: 460px;
    height: 200px;
    border-radius: 0 0 230px 230px;
    background: radial-gradient(ellipse at 50% 30%, var(--lace) 0%, rgba(230,230,234,0.5) 55%, rgba(255,255,255,0) 75%);
  }
  .sleeve {
    position: absolute;
    left: 236px;
    top: 250px;
    width: 720px;
    height: 810px;
    overflow: hidden;
    background:
      radial-gradient(circle at 18% 12%, rgba(244,182,207,0.85) 0%, rgba(244,182,207,0) 45%),
      radial-gradient(circle at 60% 10%, rgba(246,196,214,0.8) 0%, rgba(246,196,214,0) 40%),
      radial-gradient(circle at 95% 25%, rgba(207,225,243,0.9) 0%, rgba(207,225,243,0) 40%),
      radial-gradient(circle at 5% 90%, rgba(207,225,243,0.9) 0%, rgba(207,225,243,0) 45%),
      radial-gradient(circle at 60% 70%, rgba(248,237,198,0.95) 0%, rgba(248,237,198,0) 50%),
      linear-gradient(180deg, #e4cde6 0%, #f0dbe8 30%, #f3ecdc 60%, #e6ecf1 100%);
  }
  .flower {
    position: absolute;
    border-radius: 50%;
  }
  .flower--pink {
    left: -11px; top: 35px; width: 290px; height: 270px;
    background: radial-gradient(circle at 50% 50%, var(--rose) 0%, rgba(244,182,207,0.85) 22%, rgba(244,182,207,0.35) 60%, rgba(244,182,207,0) 72%);
  }
  .flower--lilac {
    left: 508px; top: 165px; width: 200px; height: 190px;
    background: radial-gradient(circle at 50% 50%, #b9a8e0 0%, rgba(201,194,234,0.7) 30%, rgba(201,194,234,0) 70%);
  }
  .flower--cream {
    left: 420px; top: 555px; width: 290px; height: 270px;
    background: radial-gradient(circle at 50% 55%, var(--cream) 0%, rgba(251,230,207,0.85) 40%, rgba(251,230,207,0) 72%);
  }
  .band {
    position: absolute;
    left: 0;
    top: 346px;
    width: 100%;
    height: 108px;
    background: var(--band);
  }
  .band__lace {
    position: absolute;
    left: 240px;
    top: 280px;
    width: 236px;
    height: 270px;
    clip-path: polygon(50% 0, 93% 24%, 93% 76%, 50% 100%, 7% 76%, 7% 24%);
    background: radial-gradient(circle at 50% 50%, #f4f0f7 0%, #ffffff 45%, #ebe8f1 100%);
  }
  .brand {
    position: absolute;
    left: 14px;
    top: 384px;
    width: 220px;
    text-align: center;
    color: var(--ink);
    white-space: nowrap;
  }
  .brand__name {
    font-family: "Cormorant Garamond", serif;
    font-weight: 600;
    font-size: 18px;
    letter-spacing: 1px;
    margin: 0;
    line-height: 1.1;
  }
  .brand__maker {
    font-family: "Cormorant Garamond", serif;
    font-size: 9px;
    letter-spacing: 2px;
    margin: 4px 0 0;
  }
  .product {
    position: absolute;
    left: 480px;
    top: 374px;
    width: 220px;
    text-align: center;
    color: var(--ink);
    white-space: nowrap;
  }
  .product__line {
    font-family: "Noto Serif KR", serif;
    font-size: 21px;
    line-height: 32px;
    margin: 0;
    letter-spacing: 1px;
  }
  .product__tag {
    font-family: "Cormorant Garamond", serif;
    font-weight: 600;
    font-size: 14px;
    letter-spacing: 0.5px;
    margin: 4px 0 0;
    color: var(--ink);
  }
</style>
</head>
<body>
<div class="canvas">
  <div class="top-lace" role="img" aria-label="은은한 회색 레이스 장식 문양"></div>

  <section class="sleeve">
    <div class="flower flower--pink" role="img" aria-label="수채화 분홍 꽃 일러스트"></div>
    <div class="flower flower--lilac" role="img" aria-label="수채화 연보라 작은 꽃 일러스트"></div>
    <div class="flower flower--cream" role="img" aria-label="수채화 크림색 꽃과 꽃술 일러스트"></div>

    <div class="band"></div>
    <div class="band__lace" role="img" aria-label="무지갯빛 육각 레이스 장식"></div>

    <div class="brand">
      <p class="brand__name">PETAL HOUR TEA</p>
      <p class="brand__maker">PUREUNGORAE</p>
    </div>

    <div class="product">
      <p class="product__line">홍삼 과일 꽃차</p>
      <p class="product__line">위드그린데이</p>
      <p class="product__tag">A SOFT BLOOM TEA</p>
    </div>
  </section>
</div>
</body>
</html>
```